Marlow Label design search/01

We need a label design for a new customers chemical products. The label is 275mm wide and 165mm high. The design will be simple with lots of space left for us to thermally print the information required on each label. This thermal print is black. From the top down 70mm the label will be white. The logo size will be about 50mm-55mm across and 40mm-45mm down. The logo position needs to be 1 of the following positions
a) Cetred at the bottom
b) Centred at the top
c) At the bottom no closer than 70mm to the right edge
The attached logo has 8 logos on it and we would like the Marlow Reagents on the left.
Requirements
Must have
- Logo
- look at attached info
Nice to have
- Simple and clean

```html
<!DOCTYPE html>
<html lang="en">
<head>
<meta charset="utf-8">
<title>Marlow Reagents – Product Label Concepts</title>
<link rel="stylesheet" href="https://fonts.googleapis.com/css2?family=Open+Sans:wght@700&display=swap">
<style>
  :root {
    --backdrop: #efe9e2;
    --label-white: #ffffff;
    --label-blush: #f8c3c7;
    --label-red: #ee3340;
    --mark-light: #ffffff;
    --mark-dark: #b01e28;
    --shadow: rgba(60, 30, 10, 0.35);
  }
  * { margin: 0; padding: 0; box-sizing: border-box; }
  html, body {
    width: 918px;
    height: 1200px;
    overflow: hidden;
    background: var(--backdrop);
    font-family: "Open Sans", Arial, sans-serif;
  }
  .sheet {
    position: relative;
    width: 918px;
    height: 1200px;
  }
  .label {
    position: absolute;
    width: 784px;
    height: 470px;
    background: linear-gradient(
      to bottom,
      var(--label-white) 0%,
      var(--label-white) 43%,
      var(--label-blush) 62%,
      var(--label-red) 100%
    );
    box-shadow: 0 6px 16px var(--shadow);
  }
  .label--light-mark { left: 67px; top: 86px; }
  .label--dark-mark  { left: 70px; top: 600px; }
  .brand-name {
    position: absolute;
    left: 0;
    right: 0;
    top: 352px;
    text-align: center;
    font-weight: 700;
    line-height: 1;
    letter-spacing: 0.04em;
  }
  .brand-name__main {
    display: block;
    font-size: 34px;
  }
  .brand-name__sub {
    display: block;
    margin-top: 8px;
    font-size: 12px;
    letter-spacing: 0.02em;
  }
  .label--light-mark .brand-name { color: var(--mark-light); }
  .label--dark-mark .brand-name  { color: var(--mark-dark); }
</style>
</head>
<body>
  <main class="sheet">
    <section class="label label--light-mark" aria-label="Label with light brand name">
      <p class="brand-name">
        <span class="brand-name__main">MARLOW</span>
        <span class="brand-name__sub">REAGENTS</span>
      </p>
    </section>
    <section class="label label--dark-mark" aria-label="Label with dark brand name">
      <p class="brand-name">
        <span class="brand-name__main">MARLOW</span>
        <span class="brand-name__sub">REAGENTS</span>
      </p>
    </section>
  </main>
</body>
</html>
```